Bref créative
KESTREL Management Consultants Stationery
Standard A4 stationery pack + Business Card
Simple
Tom Hendley
Lead Consultant
41 Cobble Quay
The Moorings
Leighton Buzzard
LU6 9RD
United Kingdom
Tom.Hendley@KestrelMC.example
www.KestrelMC.example
The finished product should allow for the text layers to be edited in case of changes of address job title etc.
The document template MUST have this information at the bottom:
Kestrel Management Consultants Limited
Registered in England No 05283716
VAT Reg No GB 627 4098 15
Logo + Tagline...
Expertise at every level

```html
<!DOCTYPE html>
<html lang="en">
<head>
<meta charset="utf-8">
<title>Kestrel Management Consultants Stationery</title>
<link href="https://fonts.googleapis.com/css2?family=Montserrat:wght@400;500&family=Open+Sans:wght@400;600&family=Tinos:ital,wght@1,700&display=swap" rel="stylesheet">
<style>
:root{
  --bg:#e6e7e9;
  --paper:#ffffff;
  --blue:#1d6cb3;
  --blue-light:#3f93d6;
  --navy:#0c2e55;
  --ink:#1b1b1b;
  --grey:#6d737a;
  --rule:#b9c4cf;
}
*{margin:0;padding:0;box-sizing:border-box}
html,body{width:1200px;height:626px;overflow:hidden;background:var(--bg)}
body{position:relative;font-family:"Open Sans",Arial,sans-serif;color:var(--ink)}
.sheet{position:absolute;background:var(--paper);box-shadow:0 2px 6px rgba(0,0,0,.18);overflow:hidden}
.wave{position:absolute;left:0;bottom:0;width:100%}
.brand{position:absolute;display:flex;align-items:center;gap:5px}
.brand-mark{width:12px;height:12px;background:var(--blue)}
.brand-name{font-family:"Montserrat",Arial,sans-serif;font-weight:400;color:var(--navy);letter-spacing:1.5px;line-height:1}
.brand-sub{position:absolute;font-size:4px;color:var(--grey);letter-spacing:.3px}
.footer-text{position:absolute;color:#fff;text-align:right;line-height:1.35}

/* business cards */
.card{width:144px;height:86px;left:24px}
.card-front{top:149px}
.card-back{top:238px}
.card .brand-name{font-size:13px}
.card .brand-mark{width:10px;height:10px}
.card-person{position:absolute;left:10px;top:32px;font-size:4.6px;line-height:1.35}
.card-person strong{font-weight:600}

/* letter & fax */
.a4{width:311px;height:427px;top:60px}
.letterhead{left:187px}
.fax{left:517px}
.a4 .brand{left:20px;top:20px}
.a4 .brand-name{font-size:19px}
.a4 .brand-mark{width:15px;height:15px}
.a4 .brand-sub{left:40px;top:42px}
.a4 .footer-text{right:16px;bottom:10px;font-size:4.6px}

.fax-head{position:absolute;left:20px;right:20px;top:60px;height:11px;background:var(--navy);color:#fff;font-size:7px;font-weight:600;padding-left:4px;line-height:11px}
.fax-grid{position:absolute;left:20px;right:20px;top:71px;border-collapse:collapse;width:271px;font-size:4.6px}
.fax-grid td{border:0.6px solid var(--rule);height:11px;padding-left:3px;color:var(--grey)}
.fax-grid td.value{width:34%}
.fax-checks{position:absolute;left:20px;top:133px;display:flex;gap:9px;font-size:4.6px;color:var(--grey)}
.fax-checks span::before{content:"";display:inline-block;width:4px;height:4px;border:0.6px solid var(--grey);margin-right:2px;vertical-align:-0.5px}

/* envelopes */
.envelope{width:319px;left:857px}
.env-front{top:67px;height:138px}
.env-back{top:211px;height:85px}
.env-dark{top:319px;height:168px}
.envelope .brand-name{font-size:13px}
.envelope .brand-mark{width:10px;height:10px}
.env-address{position:absolute;right:14px;bottom:12px;font-size:4.4px;color:var(--grey);text-align:right;line-height:1.35}
.seal{position:absolute;width:12px;height:12px;background:#fff;left:50%;margin-left:-6px}

/* compliments slip */
.slip{left:391px;top:499px;width:305px;height:97px}
.slip .brand{left:14px;top:12px}
.slip .brand-name{font-size:16px}
.slip-message{position:absolute;right:18px;bottom:12px;font-family:"Tinos","Times New Roman",serif;font-style:italic;font-weight:700;font-size:15px;color:#fff}
</style>
</head>
<body>

<!-- Business card: front -->
<section class="sheet card card-front">
  <div class="brand" style="left:10px;top:9px"><span class="brand-mark"></span><span class="brand-name">KESTREL</span></div>
  <div class="brand-sub" style="left:25px;top:22px;font-size:3.4px">Expertise at every level</div>
  <div class="card-person">
    <strong>Tom Hendley</strong><br>Lead Consultant<br><br>
    T: 01525 480 210<br>Tom.Hendley@KestrelMC.example
  </div>
  <svg class="wave" viewBox="0 0 300 100" height="30" preserveAspectRatio="none" aria-hidden="true">
    <path d="M0 45 C80 10,190 75,300 20 L300 32 C190 85,80 25,0 55Z" fill="#111"/>
    <path d="M0 55 C90 30,190 90,300 32 L300 100 L0 100Z" fill="var(--blue)"/>
  </svg>
</section>

<!-- Business card: back -->
<section class="sheet card card-back">
  <div class="brand" style="left:10px;top:9px"><span class="brand-mark"></span><span class="brand-name">KESTREL</span></div>
  <div class="brand-sub" style="left:25px;top:22px;font-size:3.4px">Management Consultants</div>
  <div class="card-person" style="top:36px;left:auto;right:10px;text-align:right;color:var(--grey)">Expertise at every level</div>
  <svg class="wave" viewBox="0 0 300 100" height="34" preserveAspectRatio="none" aria-hidden="true">
    <path d="M0 45 C80 10,190 75,300 20 L300 32 C190 85,80 25,0 55Z" fill="#111"/>
    <path d="M0 55 C90 30,190 90,300 32 L300 100 L0 100Z" fill="var(--blue)"/>
  </svg>
  <div class="footer-text" style="right:8px;bottom:5px;font-size:3.8px">41 Cobble Quay, The Moorings<br>www.KestrelMC.example</div>
</section>

<!-- Letterhead -->
<section class="sheet a4 letterhead">
  <div class="brand"><span class="brand-mark"></span><span class="brand-name">KESTREL</span></div>
  <div class="brand-sub">Expertise at every level</div>
  <svg class="wave" viewBox="0 0 300 100" height="80" preserveAspectRatio="none" aria-hidden="true">
    <path d="M0 35 C80 5,190 70,300 15 L300 26 C190 82,80 20,0 48Z" fill="#111"/>
    <path d="M0 48 C90 22,190 88,300 26 L300 100 L0 100Z" fill="var(--blue)"/>
  </svg>
  <div class="footer-text">41 Cobble Quay, The Moorings, Leighton Buzzard, LU6 9RD, United Kingdom<br>T: 01525 480 210 &nbsp; www.KestrelMC.example<br>Kestrel Management Consultants Limited · Registered in England No 05283716 · VAT Reg No GB 627 4098 15</div>
</section>

<!-- Fax sheet -->
<section class="sheet a4 fax">
  <div class="brand"><span class="brand-mark"></span><span class="brand-name">KESTREL</span></div>
  <div class="brand-sub">Expertise at every level</div>
  <div class="fax-head">FAX</div>
  <table class="fax-grid">
    <tr><td>To</td><td class="value"></td><td>From</td><td class="value"></td></tr>
    <tr><td>Fax</td><td class="value"></td><td>Pages</td><td class="value"></td></tr>
    <tr><td>Phone</td><td class="value"></td><td>Date</td><td class="value"></td></tr>
    <tr><td>Re</td><td class="value"></td><td>CC</td><td class="value"></td></tr>
  </table>
  <div class="fax-checks"><span>Urgent</span><span>For Review</span><span>Please comment</span><span>Please reply</span><span>Please recycle</span></div>
  <svg class="wave" viewBox="0 0 300 100" height="80" preserveAspectRatio="none" aria-hidden="true">
    <path d="M0 35 C80 5,190 70,300 15 L300 26 C190 82,80 20,0 48Z" fill="#111"/>
    <path d="M0 48 C90 22,190 88,300 26 L300 100 L0 100Z" fill="var(--blue)"/>
  </svg>
  <div class="footer-text">41 Cobble Quay, The Moorings, Leighton Buzzard, LU6 9RD, United Kingdom<br>T: 01525 480 210 &nbsp; www.KestrelMC.example<br>Kestrel Management Consultants Limited · Registered in England No 05283716 · VAT Reg No GB 627 4098 15</div>
</section>

<!-- Envelope: front -->
<section class="sheet envelope env-front">
  <svg style="position:absolute;left:0;top:0" width="319" height="60" viewBox="0 0 300 60" preserveAspectRatio="none" aria-hidden="true">
    <path d="M0 0 H300 V8 C220 10,180 45,150 48 C120 45,80 10,0 8Z" fill="var(--blue)"/>
    <path d="M0 8 C80 10,120 45,150 48 C180 45,220 10,300 8 V12 C220 14,180 50,150 53 C120 50,80 14,0 12Z" fill="var(--navy)"/>
  </svg>
  <div class="brand" style="left:14px;bottom:14px"><span class="brand-mark"></span><span class="brand-name">KESTREL</span></div>
  <div class="env-address">41 Cobble Quay, The Moorings<br>Leighton Buzzard, LU6 9RD</div>
</section>

<!-- Envelope: back -->
<section class="sheet envelope env-back">
  <svg style="position:absolute;left:0;top:0" width="319" height="85" viewBox="0 0 319 85" aria-hidden="true">
    <path d="M0 0 L159.5 52 L319 0" fill="none" stroke="#d3d7dc" stroke-width="1"/>
    <path d="M0 85 L130 40 M319 85 L189 40" fill="none" stroke="#e2e5e8" stroke-width="1"/>
    <circle cx="159.5" cy="50" r="5" fill="var(--blue)"/>
  </svg>
</section>

<!-- Envelope: dark flap -->
<section class="sheet envelope env-dark">
  <svg style="position:absolute;left:0;top:0" width="319" height="75" viewBox="0 0 300 75" preserveAspectRatio="none" aria-hidden="true">
    <path d="M0 0 H300 V20 C220 22,185 62,150 66 C115 62,80 22,0 20Z" fill="#141414"/>
    <path d="M0 20 C80 22,115 62,150 66 C185 62,220 22,300 20 V25 C220 27,185 68,150 72 C115 68,80 27,0 25Z" fill="var(--blue)"/>
  </svg>
  <span class="seal" style="top:38px"></span>
  <div class="brand" style="left:14px;bottom:16px"><span class="brand-mark"></span><span class="brand-name">KESTREL</span></div>
  <div class="env-address">41 Cobble Quay, The Moorings<br>Leighton Buzzard, LU6 9RD<br>www.KestrelMC.example</div>
</section>

<!-- Compliments slip -->
<section class="sheet slip">
  <div class="brand"><span class="brand-mark"></span><span class="brand-name">KESTREL</span></div>
  <div class="brand-sub" style="left:31px;top:31px">Expertise at every level</div>
  <svg class="wave" viewBox="0 0 300 100" height="55" preserveAspectRatio="none" aria-hidden="true">
    <path d="M0 30 C80 5,190 60,300 12 L300 22 C190 72,80 18,0 42Z" fill="#111"/>
    <path d="M0 42 C90 20,190 78,300 22 L300 100 L0 100Z" fill="var(--blue)"/>
  </svg>
  <div class="slip-message">With Complements</div>
</section>

</body>
</html>
```